Profesional personal website needs design and business card

I need a business card with my professional name as a logo "Marlo Vitality" for my business. I am a Wellness Coach, consultant and trainer. So it should be professional, wellness oriented and modern.

Target Market(s)

Private clients, governments, corporations. Luxury and high market.

Industry/Entity Type

Health And Wellness

Contact Information for Business Card

Marlo Vitality should be the logo

Colors

Designer to choose colors to be used in the design.

Requirements
Must have
• Marlo Vitality
• Name: Tomás Arribal
• Wellness Coach, Consultant & Trainer.
• Website: www.marlovitality.example
• Phone:
• Spain (+34) 612 480 397
• (USA) +1 (555) 318 2046
Nice to have
• The most important is the design of "Marlo Vitality", as this is going to be my personal brand logo. It should be professional, wellness, high end and actual.
Should not have
• no golds, no baroque style..

```html
<!DOCTYPE html>
<html lang="en">
<head>
<meta charset="utf-8">
<title>Marlo Vitality — Business Card</title>
<link rel="stylesheet" href="https://fonts.googleapis.com/css2?family=Marcellus&family=Open+Sans:wght@400&display=swap">
<style>
  :root {
    --page-bg: #e6e6e4;
    --card-bg: #111214;
    --card-edge: #1c1d20;
    --silver: #8e9094;
    --silver-light: #a6a8ac;
    --accent-blue: #2f8fd8;
    --contact-grey: #9a9b9e;
  }
  html, body {
    margin: 0;
    padding: 0;
    width: 1200px;
    height: 824px;
    overflow: hidden;
    background: var(--page-bg);
  }
  .canvas {
    position: relative;
    width: 1200px;
    height: 824px;
  }
  .card {
    position: absolute;
    width: 525px;
    height: 300px;
    background: linear-gradient(160deg, var(--card-edge), var(--card-bg) 60%);
    border-radius: 3px;
    box-shadow: 0 6px 18px rgba(0,0,0,0.25);
    overflow: hidden;
  }
  .card--front { left: 50px; top: 130px; }
  .card--back  { left: 625px; top: 394px; }

  .brand-dot {
    display: block;
    border-radius: 50%;
    background: var(--accent-blue);
  }
  .brand-name {
    font-family: "Marcellus", serif;
    color: var(--silver);
    margin: 0;
    font-weight: 400;
    white-space: nowrap;
  }

  /* Front */
  .front-brand {
    position: absolute;
    left: 0; right: 0; top: 70px;
    display: flex;
    flex-direction: column;
    align-items: center;
  }
  .front-brand .brand-dot { width: 46px; height: 46px; margin-bottom: 14px; }
  .front-brand .brand-name { font-size: 44px; letter-spacing: 0.5px; }
  .front-web {
    margin-top: 22px;
    font-family: "Marcellus", serif;
    font-size: 12px;
    letter-spacing: 2.5px;
    color: var(--accent-blue);
  }

  /* Back */
  .back-brand {
    position: absolute;
    left: 30px; top: 92px;
    width: 230px;
    display: flex;
    flex-direction: column;
    align-items: center;
  }
  .back-brand .brand-dot { width: 34px; height: 34px; margin-bottom: 10px; }
  .back-brand .brand-name { font-size: 27px; }

  .back-contact {
    position: absolute;
    left: 280px; top: 98px;
  }
  .person-name {
    font-family: "Marcellus", serif;
    font-size: 22px;
    color: var(--silver-light);
    margin: 0;
    font-weight: 400;
  }
  .person-title {
    font-family: "Marcellus", serif;
    font-size: 12.5px;
    color: var(--accent-blue);
    margin: 2px 0 12px;
  }
  .contact-list {
    list-style: none;
    margin: 0;
    padding: 0;
    font-family: "Open Sans", sans-serif;
    font-size: 11.5px;
    color: var(--contact-grey);
  }
  .contact-list li {
    display: flex;
    align-items: center;
    gap: 7px;
    margin-bottom: 5px;
  }
  .contact-icon { width: 11px; height: 11px; flex: none; }
</style>
</head>
<body>
<main class="canvas">

  <section class="card card--front" aria-label="Business card front">
    <div class="front-brand">
      <span class="brand-dot" aria-hidden="true"></span>
      <h1 class="brand-name">Marlo Vitality</h1>
      <div class="front-web">www.marlovitality.example</div>
    </div>
  </section>

  <section class="card card--back" aria-label="Business card back">
    <div class="back-brand">
      <span class="brand-dot" aria-hidden="true"></span>
      <p class="brand-name">Marlo Vitality</p>
    </div>
    <div class="back-contact">
      <h2 class="person-name">Tomás Arribal</h2>
      <p class="person-title">Wellness Coach, Consultant &amp; Trainer</p>
      <ul class="contact-list">
        <li>
          <svg class="contact-icon" viewBox="0 0 12 12" aria-hidden="true">
            <path d="M1 4 Q6 1 11 4 L10 5.5 L8 4.8 L8 4 Q6 3.3 4 4 L4 4.8 L2 5.5 Z" fill="#6fa6d6"/>
            <rect x="2.5" y="6" width="7" height="5" rx="1" fill="#6fa6d6"/>
          </svg>
          Spain (+34) 612 480 397
        </li>
        <li>
          <svg class="contact-icon" viewBox="0 0 12 12" aria-hidden="true">
            <path d="M1 4 Q6 1 11 4 L10 5.5 L8 4.8 L8 4 Q6 3.3 4 4 L4 4.8 L2 5.5 Z" fill="#6fa6d6"/>
            <rect x="2.5" y="6" width="7" height="5" rx="1" fill="#6fa6d6"/>
          </svg>
          (USA) +1 (555) 318 2046
        </li>
        <li>
          <svg class="contact-icon" viewBox="0 0 12 12" aria-hidden="true">
            <g fill="none" stroke="#6fa6d6" stroke-width="1">
              <circle cx="6" cy="6" r="5"/>
              <ellipse cx="6" cy="6" rx="2.2" ry="5"/>
              <line x1="1" y1="6" x2="11" y2="6"/>
            </g>
          </svg>
          www.marlovitality.example
        </li>
      </ul>
    </div>
  </section>

</main>
</body>
</html>
```